Local Roofing/Construction company business needs new biz card design

We need a new business card design, current cards are from the start of this operation and generic at best. We are a local Construction Company (General Contractor) with a majority of our work originating from insurance claims-exterior finish work is the main focus (Roofs-Siding-Gutters etc). Heavily involved with homeowners and the low ball offers they receive from insurance company's after a insurable event takes place. I have attached some of our original logo file(s) below.

```html
<!DOCTYPE html>
<html lang="en">
<head>
<meta charset="utf-8">
<title>Stonecrest Construction — Business Card</title>
<link rel="stylesheet" href="https://fonts.googleapis.com/css2?family=Jost:wght@400;500;600;700&display=swap">
<style>
  :root {
    --backdrop: #2e2f30;
    --brand-green: #4cb766;
    --brand-green-deep: #3fa85a;
    --ink-dark: #142723;
    --paper: #f4f4f4;
    --text-body: #1f1f1f;
    --rule: #6d6d6d;
    --white: #ffffff;
  }
  * { box-sizing: border-box; margin: 0; padding: 0; }
  html, body {
    width: 1200px; height: 900px; overflow: hidden;
    background: var(--backdrop);
    font-family: "Jost", "Futura", sans-serif;
  }
  .stage { position: relative; width: 1200px; height: 900px; }
  .card {
    position: absolute; left: 310px; width: 580px; height: 332px;
    border-radius: 4px; overflow: hidden;
    box-shadow: 0 12px 30px rgba(0,0,0,.45);
  }

  .brand-name {
    display: flex; align-items: center; justify-content: center; gap: 10px;
    font-weight: 700; color: var(--ink-dark); letter-spacing: 1px;
    text-transform: uppercase; white-space: nowrap; line-height: 1.1;
  }
  .brand-name__mark { background: var(--ink-dark); display: inline-block; flex: none; }

  /* Back side */
  .card--back {
    top: 88px;
    background: linear-gradient(135deg, var(--brand-green-deep), var(--brand-green) 60%, #55c070);
    color: var(--white); text-align: center;
  }
  .tagline { margin-top: 26px; font-size: 19px; font-weight: 600; letter-spacing: .2px; }
  .card--back .brand-name { margin-top: 16px; font-size: 30px; }
  .card--back .brand-name__mark { width: 20px; height: 20px; }
  .section-title {
    margin-top: 16px; font-size: 15px; font-weight: 600; color: var(--ink-dark);
    letter-spacing: .5px; text-transform: uppercase;
  }
  .services { display: flex; justify-content: center; margin-top: 4px; font-size: 15px; line-height: 1.3; }
  .services__col { padding: 0 10px; }
  .services__col--left { text-align: right; border-right: 1.5px solid var(--ink-dark); }
  .services__col--right { text-align: left; }
  .hours { margin-top: 4px; font-size: 15px; }
  .hours__sep { color: var(--ink-dark); margin: 0 4px; }
  .emergency {
    display: inline-flex; align-items: center; gap: 8px;
    margin-top: 6px; font-size: 17px; font-weight: 600; color: var(--ink-dark);
  }
  .emergency svg { width: 18px; height: 18px; }

  /* Front side */
  .card--front {
    top: 478px;
    background: linear-gradient(135deg, #ececec, var(--paper) 50%, #fbfbfb);
    color: var(--text-body);
  }
  .card--front .brand-name {
    position: absolute; top: 46px; left: 0; right: 0; font-size: 32px;
  }
  .card--front .brand-name__mark { width: 22px; height: 22px; background: var(--brand-green); }
  .rule { position: absolute; height: 1px; background: var(--rule); }
  .rule--top { top: 114px; left: 40px; right: 40px; }
  .rule--bottom { top: 226px; left: 40px; right: 40px; }
  .person { position: absolute; top: 140px; left: 52px; font-size: 21px; }
  .person__name { color: var(--brand-green); font-weight: 600; text-transform: uppercase; }
  .person__bar { color: var(--brand-green); margin: 0 6px; }
  .person__role { font-weight: 400; }
  .address {
    position: absolute; top: 136px; right: 52px; text-align: right;
    font-size: 17px; line-height: 1.35;
  }
  .contacts {
    position: absolute; top: 240px; left: 52px; list-style: none;
    font-size: 16px; line-height: 1.55;
  }
  .contacts li { display: flex; align-items: center; gap: 10px; }
  .contacts svg { width: 16px; height: 16px; flex: none; }
</style>
</head>
<body>
<main class="stage">

  <section class="card card--back" aria-label="Card back">
    <p class="tagline">You Can Trust Our 30 Years Of Combined Experience</p>
    <div class="brand-name"><span class="brand-name__mark"></span>Stonecrest Construction</div>
    <h2 class="section-title">Our Services</h2>
    <div class="services">
      <div class="services__col services__col--left">Residential Roofing<br>Exterior Finishes</div>
      <div class="services__col services__col--right">Commercial Roofing<br>Storm Restoration</div>
    </div>
    <h2 class="section-title">Connect</h2>
    <p class="hours">Monday - Friday: 8am - 6pm<span class="hours__sep">|</span>Saturday - Sunday: By Appointment Only</p>
    <div class="emergency">
      <svg viewBox="0 0 24 24" aria-hidden="true"><path fill="#142723" d="M6.6 10.8a15.1 15.1 0 0 0 6.6 6.6l2.2-2.2c.3-.3.7-.4 1-.2 1.1.4 2.3.6 3.6.6.6 0 1 .4 1 1V20c0 .6-.4 1-1 1A17 17 0 0 1 3 4c0-.6.4-1 1-1h3.5c.6 0 1 .4 1 1 0 1.3.2 2.5.6 3.6.1.3 0 .7-.2 1z"/></svg>
      Emergency: 555-418-2297
    </div>
  </section>

  <section class="card card--front" aria-label="Card front">
    <div class="brand-name"><span class="brand-name__mark"></span>Stonecrest Construction</div>
    <div class="rule rule--top"></div>
    <p class="person"><span class="person__name">Daniel Moore</span><span class="person__bar">|</span><span class="person__role">Director</span></p>
    <p class="address">48 Willow Bend<br>Ln, Fairview, MO 63021</p>
    <div class="rule rule--bottom"></div>
    <ul class="contacts">
      <li><svg viewBox="0 0 24 24" aria-hidden="true"><path fill="#4cb766" d="M6.6 10.8a15.1 15.1 0 0 0 6.6 6.6l2.2-2.2c.3-.3.7-.4 1-.2 1.1.4 2.3.6 3.6.6.6 0 1 .4 1 1V20c0 .6-.4 1-1 1A17 17 0 0 1 3 4c0-.6.4-1 1-1h3.5c.6 0 1 .4 1 1 0 1.3.2 2.5.6 3.6.1.3 0 .7-.2 1z"/></svg>555-210-4381</li>
      <li><svg viewBox="0 0 24 24" aria-hidden="true"><rect x="2" y="5" width="20" height="14" rx="1.5" fill="#4cb766"/><path d="M3 6l9 7 9-7" fill="none" stroke="#fff" stroke-width="1.6"/></svg>hello@stonecrestbuild.com</li>
      <li><svg viewBox="0 0 24 24" aria-hidden="true"><g fill="none" stroke="#4cb766" stroke-width="1.6"><circle cx="12" cy="12" r="9.5"/><ellipse cx="12" cy="12" rx="4" ry="9.5"/><path d="M2.5 12h19M4 7h16M4 17h16"/></g></svg>www.stonecrestbuild.com</li>
    </ul>
  </section>

</main>
</body>
</html>
```